Eye catching business card

2 sided
Black background with logo in color on one side along with the words "Proudly serving the commercial and defense industries since 1975"
2nd side to contain contact information (see attached current business card) and "Waterjet, Composite, Precision Machining and Clean Room Manufacturing" with a very faint watermark of a waving USA Flag in the back ground.
Remove the "est. 195" from the current logo design

```html
<!DOCTYPE html>
<html lang="en">
<head>
<meta charset="utf-8">
<title>Meridian Fabrication Inc – Business Card</title>
<link href="https://fonts.googleapis.com/css2?family=Montserrat:wght@400;500;600&display=swap" rel="stylesheet">
<style>
  :root {
    --backdrop: #2a2a2a;
    --card-black: #070707;
    --card-sheen: #1c1c1c;
    --brand-blue: #3a8fd6;
    --text-grey: #b5b5b5;
    --text-light: #d6d6d6;
    --rule-grey: #8a8a8a;
  }
  * { margin: 0; padding: 0; box-sizing: border-box; }
  html, body {
    width: 875px;
    height: 1200px;
    overflow: hidden;
    background: var(--backdrop);
    font-family: "Montserrat", sans-serif;
  }
  .canvas { position: relative; width: 875px; height: 1200px; }

  .card {
    position: absolute;
    width: 515px;
    height: 333px;
    background: linear-gradient(100deg, var(--card-sheen) 0%, var(--card-black) 35%, var(--card-black) 100%);
  }
  .card--front { left: 180px; top: 157px; }
  .card--back  { left: 180px; top: 696px; }

  /* Front */
  .front-brand {
    position: absolute;
    top: 100px;
    left: 0;
    width: 100%;
    text-align: center;
  }
  .brand-square {
    display: block;
    width: 30px;
    height: 30px;
    margin: 0 auto 18px;
    background: var(--brand-blue);
  }
  .brand-name {
    font-weight: 500;
    font-size: 19px;
    letter-spacing: 0.5px;
    color: var(--text-grey);
    line-height: 1.2;
  }
  .brand-name span { display: block; font-size: 9px; letter-spacing: 3px; margin-top: 3px; }
  .front-tagline {
    position: absolute;
    top: 232px;
    left: 0;
    width: 100%;
    text-align: center;
    font-size: 9px;
    line-height: 15px;
    color: var(--text-grey);
    text-transform: uppercase;
  }
  .front-tagline .since { font-size: 11px; color: var(--text-light); margin-top: 2px; display: block; }

  /* Back */
  .person {
    position: absolute;
    left: 56px;
    top: 62px;
  }
  .person-name { font-weight: 500; font-size: 29px; color: var(--brand-blue); line-height: 1; }
  .person-title { font-size: 16px; color: var(--text-grey); margin-top: 4px; letter-spacing: 0.3px; }
  .contact {
    position: absolute;
    left: 56px;
    top: 150px;
    list-style: none;
    font-size: 15px;
    color: var(--text-grey);
  }
  .contact li { display: flex; align-items: center; gap: 8px; height: 20px; }
  .contact svg { width: 12px; height: 12px; fill: var(--text-grey); }
  .back-brand {
    position: absolute;
    left: 300px;
    top: 95px;
    width: 180px;
    text-align: center;
    font-weight: 500;
    font-size: 24px;
    line-height: 1.25;
    color: var(--brand-blue);
  }
  .flag-art {
    position: absolute;
    left: 29px;
    top: 272px;
    width: 52px;
    height: 36px;
    background: linear-gradient(135deg, #3b5fb0 0%, #3b5fb0 40%, #c43a3f 41%, #d9d9d9 60%, #c43a3f 80%);
    opacity: 0.9;
  }
  .services-rule {
    position: absolute;
    left: 95px;
    top: 280px;
    width: 392px;
    height: 1px;
    background: var(--brand-blue);
  }
  .services {
    position: absolute;
    left: 95px;
    top: 294px;
    width: 392px;
    display: flex;
    justify-content: space-between;
    font-size: 7.6px;
    letter-spacing: 0.2px;
    color: var(--brand-blue);
    text-transform: uppercase;
  }
</style>
</head>
<body>
<main class="canvas">

  <section class="card card--front">
    <div class="front-brand">
      <span class="brand-square"></span>
      <p class="brand-name">MERIDIAN FABRICATION<span>INC</span></p>
    </div>
    <p class="front-tagline">
      Proudly serving the commercial<br>
      and defense industries
      <span class="since">Since 1975</span>
    </p>
  </section>

  <section class="card card--back">
    <div class="person">
      <h1 class="person-name">Dana Whitford</h1>
      <p class="person-title">PRESIDENT</p>
    </div>
    <ul class="contact">
      <li>
        <svg viewBox="0 0 12 12"><rect x="0" y="2" width="12" height="8" /><path d="M0 2 L6 7 L12 2" stroke="#070707" stroke-width="1" fill="none"/></svg>
        dana@meridianfab
      </li>
      <li>
        <svg viewBox="0 0 12 12"><path d="M2.5 0.5 L4.5 3 L3.3 4.6 C4 6.3 5.7 8 7.4 8.7 L9 7.5 L11.5 9.5 L10 11.5 C5 11 1 7 0.5 2 Z"/></svg>
        555-014-0172
      </li>
    </ul>
    <p class="back-brand">MERIDIAN<br>FABRICATION</p>
    <div class="flag-art" role="img" aria-label="Waving United States flag"></div>
    <div class="services-rule"></div>
    <p class="services">
      <span>Waterjet</span><span>•</span><span>Composite</span><span>•</span><span>Precision Machining</span><span>•</span><span>Clean Room Manufacturing</span>
    </p>
  </section>

</main>
</body>
</html>
```